Business Card Design Project

i need a bussines car design
Veltra Clinical Hypnotherapy

Gordon Wexley
Psychotherapy & Hypnosis

64029381 /0427956120

back of the card appoinment space.

file was provided on a PDF, LOgo , use the blu colorsa as well , elegant, clear,

Target Market(s)

young professional, caucasian , young mothers.

Industry/Entity Type

Business

```html
<!DOCTYPE html>
<html lang="en">
<head>
<meta charset="utf-8">
<title>Veltra Clinical Hypnotherapy – Business Cards</title>
<link href="https://fonts.googleapis.com/css2?family=Open+Sans:wght@400;600;700&display=swap" rel="stylesheet">
<style>
  :root {
    --stage: #e9ecef;
    --card: #ffffff;
    --blue: #0b74bd;
    --blue-deep: #1f6fb5;
    --grey: #7a7f85;
    --line: #9aa0a6;
    --badge: #6cc04a;
    --badge-ring: #f2c318;
    --photo-a: #c9b49d;
    --photo-b: #efe4d6;
  }
  * { box-sizing: border-box; margin: 0; padding: 0; }
  html, body { width: 1200px; height: 789px; overflow: hidden; }
  body {
    background: var(--stage);
    font-family: "Open Sans", Arial, sans-serif;
    position: relative;
  }
  .card {
    position: absolute;
    width: 560px;
    height: 320px;
    background: var(--card);
    box-shadow: 0 6px 18px rgba(0,0,0,.18);
    overflow: hidden;
  }
  .card--back { left: 60px; top: 70px; }
  .card--front { left: 580px; top: 400px; }

  /* Back card */
  .practice { position: absolute; left: 30px; top: 36px; width: 255px; }
  .practice__name { color: var(--blue-deep); font-weight: 700; font-size: 15px; line-height: 1.3; }
  .practice__detail { color: var(--grey); font-size: 13px; line-height: 1.35; }
  .practice__email { color: var(--grey); font-size: 10px; font-weight: 700; margin-top: 1px; }
  .reschedule {
    position: absolute; left: 36px; top: 116px; width: 236px;
    color: var(--blue-deep); font-size: 12px; line-height: 1.4; text-align: center;
  }
  .appointments { position: absolute; left: 290px; top: 22px; width: 250px; }
  .appointments__title {
    color: var(--blue-deep); font-weight: 700; font-size: 14px;
    text-align: center; margin-bottom: 4px;
  }
  .appointments__row {
    display: flex; align-items: flex-end; gap: 4px;
    color: var(--grey); font-size: 13px; height: 28px;
  }
  .blank { display: inline-block; border-bottom: 1px solid var(--line); height: 14px; }
  .blank--time { width: 26px; }
  .blank--what { width: 90px; margin-left: 4px; }
  .blank--date { width: 14px; }
  .slash { color: var(--line); }
  .back-band {
    position: absolute; left: 0; right: 0; top: 205px; height: 46px; background: var(--blue);
  }
  .registration {
    position: absolute; left: 0; right: 0; top: 262px;
    text-align: center; color: var(--blue-deep); font-size: 15px;
  }

  /* Front card */
  .brand { position: absolute; left: 40px; top: 98px; }
  .brand__mark { display: flex; align-items: center; gap: 10px; }
  .brand__dot { width: 22px; height: 22px; border-radius: 50%; background: var(--blue); }
  .brand__name { color: var(--blue); font-size: 26px; font-weight: 400; letter-spacing: .3px; }
  .brand__rule { height: 1px; background: var(--blue); margin: 6px 0 3px; width: 250px; }
  .brand__web { color: var(--grey); font-size: 9px; letter-spacing: 1px; }
  .portrait {
    position: absolute; right: 40px; top: 36px; width: 160px; height: 164px;
    background: linear-gradient(160deg, var(--photo-b), var(--photo-a));
  }
  .front-band {
    position: absolute; left: 0; right: 0; top: 200px; height: 58px; background: var(--blue);
  }
  .person { position: absolute; left: 40px; top: 208px; color: #fff; }
  .person__name { font-size: 16px; }
  .person__role { font-size: 12px; }
  .membership {
    position: absolute; right: 22px; top: 206px;
    display: flex; align-items: center; gap: 8px; color: #fff; font-size: 11px;
  }
  .membership__badge {
    width: 34px; height: 34px; border-radius: 50%;
    background: var(--badge); border: 2px solid var(--badge-ring);
  }
  .contact {
    position: absolute; right: 22px; top: 270px;
    display: flex; align-items: center; gap: 6px;
    color: var(--blue-deep); font-size: 14px;
  }
  .contact svg { width: 14px; height: 14px; }
</style>
</head>
<body>

<section class="card card--back" aria-label="Card back">
  <div class="practice">
    <p class="practice__name">VELTRA Clinical Hypnotherapy</p>
    <p class="practice__detail">By Appointment. Phone: 0427 956 120</p>
    <p class="practice__detail">48 Delmore Street, Kenlow 3127</p>
    <p class="practice__email">hello@veltraclinicalhypnotherapy.com.au</p>
  </div>
  <p class="reschedule">To reschedule your appointment,<br>please SMS or phone<br>0427 956 120 at least 24 hours prior to<br>your allocated time. Thank you.</p>

  <div class="appointments">
    <p class="appointments__title">Your Appointments</p>
    <div class="appointments__row">1.<span class="blank blank--time"></span>am/pm<span class="blank blank--what"></span><span class="blank blank--date"></span><span class="slash">/</span><span class="blank blank--date"></span><span class="slash">/</span><span class="blank blank--date"></span></div>
    <div class="appointments__row">2.<span class="blank blank--time"></span>am/pm<span class="blank blank--what"></span><span class="blank blank--date"></span><span class="slash">/</span><span class="blank blank--date"></span><span class="slash">/</span><span class="blank blank--date"></span></div>
    <div class="appointments__row">3.<span class="blank blank--time"></span>am/pm<span class="blank blank--what"></span><span class="blank blank--date"></span><span class="slash">/</span><span class="blank blank--date"></span><span class="slash">/</span><span class="blank blank--date"></span></div>
    <div class="appointments__row">4.<span class="blank blank--time"></span>am/pm<span class="blank blank--what"></span><span class="blank blank--date"></span><span class="slash">/</span><span class="blank blank--date"></span><span class="slash">/</span><span class="blank blank--date"></span></div>
    <div class="appointments__row">5.<span class="blank blank--time"></span>am/pm<span class="blank blank--what"></span><span class="blank blank--date"></span><span class="slash">/</span><span class="blank blank--date"></span><span class="slash">/</span><span class="blank blank--date"></span></div>
  </div>

  <div class="back-band"></div>
  <p class="registration">NHRB Registration No. NPM058214</p>
</section>

<section class="card card--front" aria-label="Card front">
  <div class="brand">
    <div class="brand__mark">
      <span class="brand__dot"></span>
      <span class="brand__name">Veltra Hypnotherapy</span>
    </div>
    <div class="brand__rule"></div>
    <p class="brand__web">www.veltraclinicalhypnotherapy.com.au</p>
  </div>

  <div class="portrait" role="img" aria-label="Portrait photograph of the therapist"></div>

  <div class="front-band"></div>
  <div class="person">
    <p class="person__name">Gordon Wexley</p>
    <p class="person__role">Psychotherapy &amp; Hypnosis</p>
  </div>
  <div class="membership">
    <span>Member of CHA</span>
    <span class="membership__badge" aria-hidden="true"></span>
  </div>

  <p class="contact">
    <svg viewBox="0 0 24 24" aria-hidden="true"><path fill="#1f6fb5" d="M6.6 10.8a15.1 15.1 0 0 0 6.6 6.6l2.2-2.2c.3-.3.7-.4 1-.2 1.1.4 2.3.6 3.6.6.6 0 1 .4 1 1V20c0 .6-.4 1-1 1A17 17 0 0 1 3 4c0-.6.4-1 1-1h3.5c.6 0 1 .4 1 1 0 1.3.2 2.5.6 3.6.1.3 0 .7-.2 1z"/></svg>
    64029381 /0427956120
  </p>
</section>

</body>
</html>
```